Design einer Angebotsmappe
Zielgruppe
Wir sind ein Handwerksbetrieb im Bereich Elektrotechnik.
Wir betreuen private Haushalte, Gewerbekunden oder Architekten.
Mehr über uns : www.kessler-brandau.de
Aufgabenstellung
Es soll das Design für eine Angebotsmappe erstellt werden. Die Mappe soll einen sehr hochwertigen und professionellen Eindruck beim Kunden machen.
Unser Logo soll auf der Vorderseite platziert werden und mit partiellen UV Lack in Szene gesetzt werden.
Alles andere ist Ihrer Kreativität überlassen.
-An geeigneter Stelle soll auf unsere Profile bei Instagram & Facebook hingewiesen werden mit passenden Icon und Accountname.
-Sowie ein Hinweis auf unsere Internetseite www.kessler-brandau.de
Zu beachten sind die Druckvorgaben im Anhang

```html
<!DOCTYPE html>
<html lang="de">
<head>
<meta charset="utf-8">
<title>Angebotsmappe – Kessler &amp; Brandau Elektrotechnik</title>
<link href="https://fonts.googleapis.com/css2?family=Open+Sans:wght@300;400;600&display=swap" rel="stylesheet">
<style>
  :root {
    --stage: #e2e2e2;
    --paper: #f3f4f6;
    --band: #eeeeee;
    --blue-deep: #6f9fe6;
    --blue-mid: #a9c6ee;
    --blue-soft: #d6e3f3;
    --brand: #2e9fd6;
    --ink: #2a2a2a;
    --muted: #b4b4b4;
  }
  * { margin: 0; padding: 0; box-sizing: border-box; }
  html, body { width: 1200px; height: 1200px; overflow: hidden; }
  body {
    background: var(--stage);
    font-family: "Open Sans", Arial, sans-serif;
    display: flex; align-items: center; justify-content: center;
  }
  .folder-cover {
    position: relative;
    width: 720px; height: 1018px;
    background: var(--paper);
    overflow: hidden;
    box-shadow: 0 14px 36px rgba(0,0,0,0.12);
  }
  .cover-artwork {
    position: absolute; inset: 0;
    background:
      radial-gradient(circle at 72% 38%, rgba(243,244,246,1) 0%, rgba(236,240,246,0.95) 22%, rgba(214,227,243,0.7) 40%, rgba(169,198,238,0) 62%),
      linear-gradient(120deg, var(--blue-deep) 0%, var(--blue-mid) 35%, var(--blue-soft) 60%, var(--paper) 85%);
  }
  .footer-band {
    position: absolute; left: 250px; right: 0; bottom: 0; height: 262px;
    background: var(--band);
  }
  .brand {
    position: absolute; top: 250px; left: 300px; width: 360px;
    text-align: center; color: var(--brand);
  }
  .brand-dot {
    width: 64px; height: 64px; border-radius: 50%;
    border: 5px solid var(--brand);
    margin: 0 auto 14px;
  }
  .brand-name {
    font-size: 30px; font-weight: 600; letter-spacing: 1.5px;
    text-transform: uppercase; line-height: 1.1;
  }
  .brand-line {
    font-size: 12px; font-weight: 600; letter-spacing: 4px;
    text-transform: uppercase; margin-top: 6px;
    border-bottom: 1px solid var(--brand); padding-bottom: 6px;
  }
  .cover-title {
    position: absolute; left: 420px; top: 700px;
  }
  .cover-title h1 {
    font-size: 30px; font-weight: 400; letter-spacing: 4px; color: var(--ink);
  }
  .cover-title p {
    margin-top: 8px; font-size: 14px; font-weight: 400; line-height: 1.35;
    color: var(--muted); letter-spacing: 0.5px;
  }
</style>
</head>
<body>
  <main class="folder-cover">
    <div class="cover-artwork" role="img" aria-label="Abstraktes blaues Netzwerkmuster aus Linien und Punkten, zur Mitte hin weiß auslaufend"></div>
    <div class="footer-band"></div>

    <div class="brand">
      <div class="brand-dot"></div>
      <div class="brand-name">Kessler &amp; Brandau</div>
      <div class="brand-line">Elektrotechnik</div>
    </div>

    <div class="cover-title">
      <h1>ANGEBOT</h1>
      <p>Lorem ipsum dolor sit amet,<br>consectetur adipisicing elit sed do</p>
    </div>
  </main>
</body>
</html>
```